Young Accounting firm needing a captivating business card

We need a business card design that forces the person to look at the card because its either gold foil, plastic, or lettering pop up etc. We already have a logo with a specific gold color and we need to make it pop. We are an accounting firm. I need the words" accounting, payroll, licenses, audits, taxes" somewhere on the business card so as to describe what we do- preferably on the side where the logo is at.

Industry/Entity Type

Accounting

Contact Information for Business Card

Address 48276 9th Ave S Ste 305, Cedar Hollow, OR 98117
Business Phone (360)418-2096
Fax (360)418-2157
Office Cell Phone (360)586-7319

Font styles to use
Serif

Colors
85abd2

Requirements
Must have
• It should state
• "Accounting" "Taxes" "Audits" "Licenses" "Payroll"
Nice to have
• Matte with gold foil, different textures, With Either a textured ivory background or gray blue slate background
Should not have
• colorful colors

```html
<!DOCTYPE html>
<html lang="en">
<head>
<meta charset="utf-8">
<title>MVTallytax Business Card</title>
<link rel="stylesheet" href="https://fonts.googleapis.com/css2?family=Lato:wght@400;700&display=swap">
<style>
  :root {
    --backdrop: #d6d6d6;
    --gold: #bfa224;
    --gold-deep: #a68b18;
    --gold-ink: #b8991c;
    --paper: #fbfbfa;
    --ink: #1e1e1e;
    --white: #ffffff;
  }
  * { box-sizing: border-box; margin: 0; padding: 0; }
  html, body {
    width: 1200px; height: 900px; overflow: hidden;
    background: var(--backdrop);
    font-family: "Lato", sans-serif;
  }
  .canvas { position: relative; width: 1200px; height: 900px; }

  .card {
    position: absolute;
    width: 540px; height: 310px;
    border-radius: 22px;
    box-shadow: 0 8px 22px rgba(0,0,0,0.18);
    overflow: hidden;
  }

  /* Front: gold card */
  .card-front {
    left: 80px; top: 120px;
    background: var(--gold);
    display: flex; flex-direction: column; align-items: center; justify-content: center;
  }
  .front-brand {
    display: flex; align-items: center; gap: 14px;
    margin-top: 10px;
  }
  .front-brand .brand-mark {
    width: 28px; height: 28px;
    background: var(--gold-deep);
  }
  .front-brand .brand-name {
    font-size: 50px; font-weight: 400;
    color: var(--gold-deep);
    letter-spacing: 1px;
  }
  .services {
    position: absolute; bottom: 34px; left: 0; right: 0;
    text-align: center;
    color: var(--white);
    font-size: 14px; letter-spacing: 2.2px;
  }
  .services .dot { margin: 0 6px; }

  /* Back: white card */
  .card-back {
    left: 580px; top: 470px;
    background: var(--paper);
    padding: 40px 36px;
  }
  .back-brand { display: flex; align-items: center; gap: 10px; }
  .back-brand .brand-mark { width: 20px; height: 20px; background: var(--gold-ink); }
  .back-brand .brand-name {
    font-size: 36px; font-weight: 400; color: var(--gold-ink); letter-spacing: 0.5px;
  }
  .person { margin-top: 20px; }
  .person-name {
    font-size: 22px; font-weight: 700; color: var(--gold-ink); letter-spacing: 1px;
  }
  .person-role { font-size: 16px; color: var(--ink); margin-top: 2px; }
  .contact-list { list-style: none; margin-top: 12px; }
  .contact-list li {
    display: flex; align-items: center; gap: 8px;
    font-size: 16px; color: var(--ink); line-height: 22px;
  }
  .contact-list svg { width: 14px; height: 14px; flex: none; fill: var(--gold-ink); }
  .address {
    position: absolute; right: 36px; top: 150px;
    text-align: right; font-size: 15px; line-height: 21px; color: var(--ink);
    font-style: normal;
  }
</style>
</head>
<body>
<main class="canvas">

  <section class="card card-front" aria-label="Business card front">
    <div class="front-brand">
      <span class="brand-mark" aria-hidden="true"></span>
      <span class="brand-name">MVTallytax</span>
    </div>
    <p class="services">
      <span class="dot">•</span>ACCOUNTING<span class="dot">•</span>TAXES<span class="dot">•</span>AUDITS<span class="dot">•</span>LICENSES<span class="dot">•</span>PAYROLL
    </p>
  </section>

  <section class="card card-back" aria-label="Business card back">
    <div class="back-brand">
      <span class="brand-mark" aria-hidden="true"></span>
      <span class="brand-name">MVTallytax</span>
    </div>
    <div class="person">
      <p class="person-name">DANA REYES</p>
      <p class="person-role">Managing Director</p>
    </div>
    <ul class="contact-list">
      <li>
        <svg viewBox="0 0 16 16" aria-label="Phone"><path d="M3 1h3l1.5 4-2 1.3a9 9 0 0 0 4.2 4.2L11 8.5l4 1.5v3a2 2 0 0 1-2 2A12 12 0 0 1 1 3a2 2 0 0 1 2-2z"/></svg>
        (360)418-2096
      </li>
      <li>
        <svg viewBox="0 0 16 16" aria-label="Fax"><path d="M4 1h8v4H4zM1 6h14v7H1zM4 11h8v4H4z"/></svg>
        (360)418-2157
      </li>
      <li>
        <svg viewBox="0 0 16 16" aria-label="Cell"><path d="M4 1h8v14H4zM5.5 2.5v9h5v-9z"/></svg>
        (360)586-7319
      </li>
      <li>
        <svg viewBox="0 0 16 16" aria-label="Email"><path d="M1 3h14v10H1zM2.5 4.5 8 9l5.5-4.5z"/></svg>
        hello@mvtallytax.com
      </li>
    </ul>
    <address class="address">
      48276 9th Ave S Ste 305<br>
      Cedar Hollow, OR 98117
    </address>
  </section>

</main>
</body>
</html>
```